Velmora Company needs a Business Card Design

We just opened our business recently and we need a business card design. Our basic product are clothes and accessories. We would like to see designs that use bright colors like pink, light blue and purple. In addition to that kindly include also our address in the business card which our main office is located in Los Angeles, California.
The final design should communicate that we have affordable price yet high quality brand.

Target Market(s)

young and middle age women

Industry/Entity Type

Business

Contact Information for Business Card

Velmora Apparel and Accessories 3847 North Hollis St. Los Angeles California
Tel: 424-583-6094

Logo Text

Velmora's Apparel and Accessories

Font styles to use
Serif

Requirements
Must have
• there should be a graphic of a sexy lady wearing an elegant dress at the upper left corner of the business card.

```html
<!DOCTYPE html>
<html lang="en">
<head>
<meta charset="utf-8">
<title>Velmora Apparel and Accessories – Business Card</title>
<link rel="stylesheet" href="https://fonts.googleapis.com/css2?family=Oranienbaum&display=swap">
<style>
  :root {
    --card-white: #ffffff;
    --brand-magenta: #b3236f;
    --ink-black: #1c1c1c;
    --figure-pink: #e0148c;
    --figure-grey: #d4d4d7;
  }
  html, body {
    margin: 0;
    padding: 0;
    width: 1200px;
    height: 676px;
    overflow: hidden;
    background: var(--card-white);
  }
  .business-card {
    position: relative;
    width: 1200px;
    height: 676px;
    overflow: hidden;
    background: var(--card-white);
  }
  .fashion-figure {
    position: absolute;
    left: 170px;
    top: 70px;
    width: 280px;
    height: 540px;
    background: linear-gradient(170deg, var(--figure-grey) 0%, var(--figure-pink) 45%, var(--figure-grey) 100%);
    opacity: 0.85;
  }
  .brand-block {
    position: absolute;
    left: 490px;
    top: 235px;
    width: 680px;
  }
  .brand-name {
    margin: 0;
    font-family: "Oranienbaum", serif;
    font-weight: 400;
    font-size: 84px;
    line-height: 1.05;
    letter-spacing: 2px;
    text-transform: uppercase;
    white-space: nowrap;
    color: var(--brand-magenta);
  }
  .contact-line {
    margin: 22px 0 0;
    font-family: "Oranienbaum", serif;
    font-size: 20px;
    letter-spacing: 0.3px;
    text-transform: uppercase;
    white-space: nowrap;
    color: var(--ink-black);
  }
</style>
</head>
<body>
  <main class="business-card">
    <div class="fashion-figure" role="img" aria-label="Fashion sketch of an elegant woman in a flowing pink dress with black accents"></div>
    <section class="brand-block">
      <h1 class="brand-name">Velmora Apparel<br>and Accessories</h1>
      <p class="contact-line">3847 North Hollis St. Los Angeles California Tel: 424-583-6094</p>
    </section>
  </main>
</body>
</html>
```